Certified Notary Signing Agent Business Card Design

I need a modern, visually appealing two-sided business card for my mobile notary signing agent business which clearly communicates my certification by the Federal Sealwork Guild ("FSG") and Deed Closing Method ("DCM"). It should be clean and easy to read and trust focused. While I am not committed to specific fonts and colors, I do like the colors in both my final logo and a sample logo (color examples only). I want to hand out a business card that is easy to locate in a stack and differentiates itself easily from others as it is an extremely crowded market space.

Target Market(s)

Title Companies, Escrow Officers, Real Estate Agents, Real Estate Lenders

Industry/Entity Type

Real Estate Lending

Contact Information for Business Card

I need a two-sided business card for my mobile notary signing agent business that prominently displays my photo, logo (potentially, just on the back), my service areas, phone, email, url and an FSG certification and DCM certification. On the back side of the card I would like my url, logo and potentially certification icons. On the back, I MAY want to add language that I have been an FSG Certified NSA for 10 + years and have performed over 8k in real estate loan transactions. I have attached a very old biz card circa 2007 that I designed myself on a card ordering platform. While it's not great, it can display how I crammed all of the data on a single card. I am NOT suggesting replicating this design in any form but provide it as reference material only,

Font styles to use
Sans Serif

Requirements
Must have
• Name: Marla Vostrick, Certified Notary Signing Agent Phone: 936.555.0142 URL: www.PrimeQuillSigners.com Email: marla@primequillsigners.com, Counties serviced: Montgomery, Grimes, N. Harris, Walker, Waller, Federal Sealwork Guild Badge, Deed Closing Method Badge (still need to upload this)
Nice to have
• I am open to color variations on my logo as illustrated in the attachment labeled as Logo Sample Colors Only (11A) that has a slate blue/grey background w/white lettering and gold pen and circles

```html
<!DOCTYPE html>
<html lang="en">
<head>
<meta charset="utf-8">
<title>Prime Quill Signing Agents – Business Card</title>
<link href="https://fonts.googleapis.com/css2?family=Inter:wght@400;500;600&display=swap" rel="stylesheet">
<style>
  :root {
    --page: #f1f1f1;
    --navy: #0e1a36;
    --gold: #d4a24a;
    --white: #ffffff;
    --card-white: #fbfbfb;
    --seal-red: #e23a3f;
    --seal-blue: #1d3a7a;
    --photo-a: #8f8aa0;
    --photo-b: #c9a889;
  }
  * { box-sizing: border-box; margin: 0; padding: 0; }
  html, body { width: 1200px; height: 1000px; overflow: hidden; }
  body {
    background: var(--page);
    font-family: "Inter", Arial, sans-serif;
    position: relative;
  }
  .card {
    position: absolute;
    left: 173px;
    width: 854px;
    height: 337px;
    box-shadow: 0 3px 8px rgba(0,0,0,0.18);
    overflow: hidden;
  }
  .card-front { top: 155px; background: var(--navy); }
  .card-back { top: 507px; height: 338px; background: var(--card-white); }

  .company {
    position: absolute; left: 45px; top: 34px;
    color: var(--white); font-size: 24px; font-weight: 400;
  }
  .company-rule {
    position: absolute; left: 45px; top: 72px; width: 225px; height: 2px;
    background: linear-gradient(90deg, var(--gold), rgba(212,162,74,0));
  }
  .agent-name {
    position: absolute; left: 45px; top: 92px;
    color: var(--gold); font-size: 44px; font-weight: 500; letter-spacing: 0.3px;
  }
  .agent-title {
    position: absolute; left: 47px; top: 150px;
    color: var(--gold); font-size: 24px; font-weight: 400;
  }
  .contact-row {
    position: absolute; left: 45px; display: flex; align-items: center; gap: 12px;
    color: var(--white); font-size: 21px;
  }
  .contact-row.phone { top: 198px; }
  .contact-row.area { top: 278px; gap: 10px; font-size: 16px; line-height: 21px; }
  .icon { width: 28px; height: 28px; flex: none; }
  .contact-row.area .icon { width: 32px; height: 32px; }

  .portrait {
    position: absolute; left: 555px; top: 27px; width: 205px; height: 205px;
    border-radius: 50%; border: 3px solid var(--gold);
    background: radial-gradient(circle at 50% 45%, var(--photo-b) 0 35%, var(--photo-a) 75%);
  }
  .seal { position: absolute; }
  .card-front .seal { left: 712px; top: 193px; width: 124px; height: 124px; }
  .card-back .seal { left: 708px; top: 95px; width: 108px; height: 108px; }

  .back-art { position: absolute; inset: 0; }
  .brand {
    position: absolute; left: 95px; top: 135px; width: 240px;
    display: flex; align-items: center; gap: 12px;
  }
  .brand-dot { width: 22px; height: 22px; border-radius: 50%; background: var(--gold); flex: none; }
  .brand-name { color: var(--navy); font-size: 32px; font-weight: 600; white-space: nowrap; }

  .web-block {
    position: absolute; left: 360px; top: 110px; width: 330px; text-align: center;
    color: var(--gold); font-size: 22px;
  }
  .web-rule {
    position: relative; height: 1px; background: var(--gold); margin: 18px 6px 16px;
  }
  .web-rule::after {
    content: ""; position: absolute; left: 50%; top: -4px; width: 8px; height: 8px;
    background: var(--gold); transform: translateX(-50%) rotate(45deg);
  }
</style>
</head>
<body>

<section class="card card-front">
  <div class="company">Prime Quill Signing Agents</div>
  <div class="company-rule"></div>
  <h1 class="agent-name">Marla D. Vostrick</h1>
  <div class="agent-title">Notary Signing Agent</div>

  <div class="contact-row phone">
    <svg class="icon" viewBox="0 0 28 28"><circle cx="14" cy="14" r="12.5" fill="none" stroke="#d4a24a" stroke-width="1.6"/><path d="M9.5 8.5c1-1 2-1 2.6 0l1 1.7c.4.7.2 1.4-.4 1.9l-.7.6c.6 1.5 1.8 2.7 3.3 3.3l.6-.7c.5-.6 1.2-.8 1.9-.4l1.7 1c1 .6 1 1.6 0 2.6-1.2 1.2-3 1.3-5.4-.3-2-1.4-3.5-2.9-4.9-4.9-1.6-2.4-1.5-4.2-.3-5.4z" fill="none" stroke="#d4a24a" stroke-width="1.4"/></svg>
    <span>936.555.0142</span>
  </div>
  <div class="contact-row area">
    <svg class="icon" viewBox="0 0 32 32"><circle cx="16" cy="16" r="14.5" fill="none" stroke="#d4a24a" stroke-width="1.6"/><path d="M16 24s-5.5-6-5.5-10a5.5 5.5 0 0 1 11 0c0 4-5.5 10-5.5 10z" fill="#d4a24a"/><circle cx="16" cy="14" r="2" fill="#0e1a36"/></svg>
    <span>Serving the following Counties: Montgomery, Grimes,<br>N. Harris, Walker, Waller</span>
  </div>

  <div class="portrait" role="img" aria-label="Portrait photo of the notary signing agent"></div>
  <svg class="seal" viewBox="0 0 124 124" role="img" aria-label="Certification badge">
    <circle cx="62" cy="62" r="60" fill="var(--seal-red)"/>
    <circle cx="62" cy="62" r="48" fill="#ffffff"/>
    <circle cx="62" cy="62" r="42" fill="none" stroke="var(--seal-blue)" stroke-width="2"/>
  </svg>
</section>

<section class="card card-back">
  <svg class="back-art" viewBox="0 0 854 338" preserveAspectRatio="none">
    <path d="M0 0 H14 C30 110 20 250 150 298 C320 335 600 280 854 232 V338 H0 Z" fill="var(--navy)"/>
    <path d="M14 0 C30 110 20 250 150 298 C320 335 600 280 854 232" fill="none" stroke="var(--gold)" stroke-width="4"/>
  </svg>

  <div class="brand">
    <span class="brand-dot"></span>
    <span class="brand-name">Prime Quill</span>
  </div>

  <div class="web-block">
    <div class="email">marla@primequillsigners.com</div>
    <div class="web-rule"></div>
    <div class="url">www.primequillsigners.com</div>
  </div>

  <svg class="seal" viewBox="0 0 124 124" role="img" aria-label="Certification badge">
    <circle cx="62" cy="62" r="60" fill="var(--seal-red)"/>
    <circle cx="62" cy="62" r="48" fill="#ffffff"/>
    <circle cx="62" cy="62" r="42" fill="none" stroke="var(--seal-blue)" stroke-width="2"/>
  </svg>
</section>

</body>
</html>
```